Brochure for Hot Air Ballooning Tour Company

We need a DL trifold brochure designed. We would like to maintain our company colors and provide a vibrant and colorful brochure to the audience whilst also maintaining a professional feel.

Our website www.skyhaventours.com.au will contain some information which can be used.

We offer:
Daily Flights over the Hunter Valley
Champagne Breakfast
Digital Flight Photos
Corporate Flgihts
Private Flights
Gift Vouchers

Company Key points to mention:
Award Winning Service
Family owned and operated business
Refundable Flight Tickets

Industry/Entity Type

Tourism

Contact Information for Business Card

See existing card design, details to be the same just with same look as brochure.

Font styles to use
Sans Serif

Colors
33a6d7
ffffff
000000

Requirements
Must have
• Company Colours and feel like vehicle image, Balloon Images,

```html
<!DOCTYPE html>
<html lang="en">
<head>
<meta charset="utf-8">
<title>Sky Haven Tours – Business Card</title>
<link href="https://fonts.googleapis.com/css2?family=Montserrat:ital,wght@0,400;0,600;0,700;1,400;1,800&display=swap" rel="stylesheet">
<style>
  :root {
    --sky: #33a6d7;
    --sky-light: #8fe4fb;
    --sky-deep: #2d93c8;
    --ink: #0e1112;
    --paper: #ffffff;
    --stage: #d5dcdc;
    --rule: #e3e6e6;
    --muted-square: #c9d0d3;
  }
  * { margin: 0; padding: 0; box-sizing: border-box; }
  html, body { width: 957px; height: 1200px; overflow: hidden; }
  body {
    background: radial-gradient(ellipse at 50% 50%, #eef1f1 0%, var(--stage) 75%);
    font-family: "Montserrat", sans-serif;
    position: relative;
  }
  .card {
    position: absolute;
    left: 77px;
    width: 805px;
    height: 482px;
    overflow: hidden;
    box-shadow: 0 3px 8px rgba(0,0,0,0.25);
  }
  .card--front { top: 77px; background: var(--ink); }
  .card--back { top: 629px; background: var(--paper); }
  .card__waves { position: absolute; inset: 0; width: 100%; height: 100%; }
  .side-label {
    position: absolute;
    right: 75px;
    font-size: 29px;
    color: #1d1d1d;
    letter-spacing: 0.5px;
  }
  .side-label--front { top: 572px; }
  .side-label--back { top: 1126px; }

  .brand {
    position: absolute;
    display: flex;
    align-items: center;
    gap: 12px;
    font-weight: 700;
    white-space: nowrap;
  }
  .brand__dot { border-radius: 50%; flex: none; }
  .card--front .brand {
    left: 0; right: 0; justify-content: center;
    top: 205px;
    font-size: 58px;
    color: var(--sky);
  }
  .card--front .brand__dot { width: 40px; height: 40px; background: var(--sky); }
  .card--back .brand {
    left: 40px; width: 330px; justify-content: center;
    top: 168px;
    font-size: 32px;
    color: var(--ink);
  }
  .card--back .brand__dot { width: 26px; height: 26px; background: var(--ink); }
  .hotline {
    position: absolute;
    left: 40px; width: 330px; text-align: center;
    top: 262px;
    font-size: 32px;
    font-style: italic;
    font-weight: 800;
    color: var(--ink);
  }
  .hotline__digits { color: var(--sky); }
  .divider {
    position: absolute;
    left: 435px; top: 100px;
    width: 2px; height: 300px;
    background: linear-gradient(var(--paper), var(--rule) 20%, var(--rule) 80%, var(--paper));
  }
  .contact { position: absolute; left: 506px; top: 128px; color: var(--ink); }
  .contact__name { font-size: 19px; font-weight: 600; color: var(--sky); }
  .contact__role { font-size: 14px; font-style: italic; margin-top: 2px; }
  .contact__list { list-style: none; margin-top: 46px; font-size: 14.5px; }
  .contact__list li { display: flex; align-items: center; gap: 5px; height: 36px; }
  .contact__icon { width: 14px; height: 14px; flex: none; }
  .social { display: flex; align-items: center; gap: 11px; margin-top: 8px; font-size: 14.5px; }
  .social__label { margin-right: 1px; }
  .social__square { width: 29px; height: 29px; border-radius: 4px; background: var(--muted-square); }
</style>
</head>
<body>

<section class="card card--front">
  <svg class="card__waves" viewBox="0 0 1006 602" preserveAspectRatio="none" aria-hidden="true">
    <defs>
      <linearGradient id="swoosh" x1="0" y1="0" x2="1" y2="0">
        <stop offset="0" stop-color="#8fe4fb"/>
        <stop offset="0.5" stop-color="#2d93c8"/>
        <stop offset="1" stop-color="#8fe4fb"/>
      </linearGradient>
    </defs>
    <path d="M180,0 C330,40 470,170 650,172 C800,174 920,140 1006,118 L1006,62 C900,120 760,150 650,130 C560,112 480,40 420,0 Z" fill="url(#swoosh)"/>
    <path d="M420,0 C480,40 560,112 650,130 C760,150 900,120 1006,62 L1006,72 C900,128 760,160 650,140 C555,122 470,45 405,0 Z" fill="#ffffff"/>
    <path d="M0,418 C170,360 380,392 560,466 S880,612 1006,438 V602 H0 Z" fill="#ffffff"/>
    <path d="M0,448 C170,382 380,402 560,476 S880,618 1006,452 V602 H0 Z" fill="#33a6d7"/>
    <path d="M0,505 C170,398 380,410 580,488 S880,622 1006,470 V602 H0 Z" fill="#0e1112"/>
  </svg>
  <div class="brand"><span class="brand__dot"></span>Sky Haven Tours</div>
</section>
<div class="side-label side-label--front">Front</div>

<section class="card card--back">
  <svg class="card__waves" viewBox="0 0 1006 602" preserveAspectRatio="none" aria-hidden="true">
    <defs>
      <linearGradient id="swoosh-back" x1="0" y1="0" x2="1" y2="0">
        <stop offset="0" stop-color="#8fe4fb"/>
        <stop offset="0.5" stop-color="#2d93c8"/>
        <stop offset="1" stop-color="#8fe4fb"/>
      </linearGradient>
    </defs>
    <path d="M500,0 C570,40 650,95 760,95 C860,95 940,75 1006,55 V0 Z" fill="#0e1112"/>
    <path d="M290,0 C420,40 540,120 680,122 C820,124 930,90 1006,62 L1006,55 C940,75 860,95 760,95 C650,95 570,40 500,0 Z" fill="url(#swoosh-back)"/>
    <path d="M500,0 C570,40 650,95 760,95 C860,95 940,75 1006,55 L1006,62 C935,85 860,104 760,104 C645,104 560,45 488,0 Z" fill="#ffffff"/>
    <path d="M0,448 C170,382 380,402 560,476 S880,618 1006,452 V602 H0 Z" fill="#33a6d7"/>
    <path d="M0,505 C170,398 380,410 580,488 S880,622 1006,470 V602 H0 Z" fill="#0e1112"/>
  </svg>
  <div class="brand"><span class="brand__dot"></span>Sky Haven Tours</div>
  <div class="hotline"><span class="hotline__digits">1300</span> UP HIGH</div>
  <div class="divider"></div>
  <div class="contact">
    <div class="contact__name">Name Goes Here</div>
    <div class="contact__role">Designation</div>
    <ul class="contact__list">
      <li><svg class="contact__icon" viewBox="0 0 14 14"><circle cx="7" cy="7" r="7" fill="var(--sky)"/><path d="M4.5,3.5 L6,3.5 L6.6,5.4 L5.7,6.1 C6.2,7.1 6.9,7.8 7.9,8.3 L8.6,7.4 L10.5,8 L10.5,9.5 C7,9.8 4.2,7 4.5,3.5 Z" fill="#fff"/></svg>1300 555 019</li>
      <li><svg class="contact__icon" viewBox="0 0 14 14"><circle cx="7" cy="7" r="7" fill="var(--sky)"/><rect x="3.5" y="4.5" width="7" height="5" fill="none" stroke="#fff" stroke-width="1"/><path d="M3.5,4.5 L7,7.3 L10.5,4.5" fill="none" stroke="#fff" stroke-width="1"/></svg>info@skyhaventours.com.au</li>
      <li><svg class="contact__icon" viewBox="0 0 14 14"><circle cx="7" cy="7" r="7" fill="var(--sky)"/><circle cx="7" cy="7" r="3.8" fill="none" stroke="#fff" stroke-width="0.9"/><ellipse cx="7" cy="7" rx="1.6" ry="3.8" fill="none" stroke="#fff" stroke-width="0.9"/><line x1="3.2" y1="7" x2="10.8" y2="7" stroke="#fff" stroke-width="0.9"/></svg>www.skyhaventours.com.au</li>
    </ul>
    <div class="social">
      <span class="social__label">Visit us on :</span>
      <span class="social__square"></span>
      <span class="social__square"></span>
      <span class="social__square"></span>
    </div>
  </div>
</section>
<div class="side-label side-label--back">Back</div>

</body>
</html>
```